WP website design (N Kentucky)

We need a wordpress design that will incorporate a professional color scheme with company logo in a clean layout. The design needs to consider that this will be developed on a responsive theme. Colors are undetermined - can use a dark red - logo is black so creative use of colors will be important. Client wants a 'modern' look.
Updates

Project Deadline Extended
Reason: Client wants a few more designs

Industry/Entity Type

It Company

Font styles to use
Serif
Sans Serif

Requirements
Must have
• Must Have:
- Navigation: 1) Home 2) Auctions 3) Auction Marketing 4) Buying at Auction 5) About Us 6) Contact Us

Site will have a slideshow element and the following widgets: 1) Featured Auctions 2) Testimonials blog widget 3) 'Auction Alerts' email sign up 4) Fz Chirpa Zelnix+ icons. Colors can be the meadowline7 gold/black from http://www.brambleridgehouses.example/

In the footer, there will be smaller company logo, the affiliations logo, and contact info below:
Copperfield Gavel Sales, LLC / Wes Pellham
email: wespell@mailbox.example; wes.pellham@ml7.example
phone: (859) 555-0147 mobile phone: (859)555-0182
Domain: http://www.copperfieldgavelsales.example/
Nice to have
• - - Site will have drop-down menus - please indicate the styling, for instance the dropdown menus 1) Upcoming Auctions 2) Past Auctions under the 'Auctions' link

```html
<!DOCTYPE html>
<html lang="en">
<head>
<meta charset="utf-8">
<title>Copperfield Gavel Sales</title>
<link rel="stylesheet" href="https://fonts.googleapis.com/css2?family=Marcellus+SC&family=Roboto:ital,wght@0,400;0,500;0,700;1,400&family=Roboto+Condensed:wght@400;500&family=Source+Sans+3:wght@400;600&display=swap">
<style>
:root{
  --page:#111111;
  --red:#9b1111;
  --red-dark:#6e0b0b;
  --red-light:#b81c1c;
  --white:#ffffff;
  --panel:#eeeeee;
  --panel-line:#bdbdbd;
  --ink:#222222;
  --muted:#555555;
  --accent:#8e0f0f;
}
*{box-sizing:border-box;margin:0;padding:0}
html,body{width:997px;height:1200px;overflow:hidden;background:var(--page);font-family:Roboto,Arial,sans-serif;color:var(--ink)}
.site{position:relative;width:831px;height:1200px;margin-left:83px}
.header{position:absolute;top:0;left:0;width:831px;height:105px}
.brand{position:absolute;left:2px;top:32px;display:flex;align-items:center;gap:10px}
.brand-mark{width:30px;height:30px;border-radius:50%;background:#bdbdbd}
.brand-name{font-family:"Marcellus SC",serif;font-size:22px;color:var(--white);letter-spacing:.5px}
.social{position:absolute;right:12px;top:40px;display:flex;gap:16px}
.social a{display:flex;align-items:center;gap:6px;color:var(--white);text-decoration:none;font-size:13px;font-family:Roboto,sans-serif}
.social a span{width:18px;height:18px;border-radius:50%;background:#d5d5d5;border:2px solid #777}
.nav{position:absolute;top:105px;left:0;width:831px;height:41px;background:linear-gradient(#b01616,var(--red) 55%,var(--red-dark));border-radius:5px 5px 0 0;display:flex}
.nav a{display:flex;align-items:center;justify-content:center;height:41px;color:var(--white);text-decoration:none;font-family:"Roboto Condensed",sans-serif;font-size:13.5px;text-transform:uppercase;border-right:1px solid #7a0c0c}
.nav a:last-child{border-right:0}
.nav a.active{background:#111}
.dropdown{position:absolute;top:146px;left:103px;width:163px;z-index:5;border-bottom:3px solid var(--red)}
.dropdown a{display:block;height:30px;line-height:30px;padding-left:8px;color:var(--white);text-decoration:none;font-family:"Source Sans 3",sans-serif;font-size:13.5px}
.dropdown .upcoming{background:var(--red)}
.dropdown .past{background:#000}
.main{position:absolute;top:146px;left:0;width:831px;height:921px;background:var(--white)}
.slider{position:absolute;left:9px;top:7px;width:535px;height:222px;background:linear-gradient(180deg,#9cc3e6 0%,#d9e6f2 30%,#a33426 45%,#8b2a1f 70%,#4f6a30 85%,#6c7f3c 100%)}
.share{position:absolute;right:16px;top:10px}
.dots{position:absolute;left:210px;bottom:14px;display:flex;gap:12px}
.dots i{width:13px;height:13px;border-radius:50%;background:var(--red)}
.dots i.on{background:#e8e8e8}
.alerts{position:absolute;left:562px;top:7px;width:257px;height:221px;background:#000;color:var(--white);padding:20px 16px;font-family:"Source Sans 3",sans-serif}
.alerts h2{font-weight:400;font-size:26px;margin-bottom:12px}
.alerts p{font-size:13px;line-height:17px;margin-bottom:10px}
.alerts .email{display:block;width:204px;height:29px;background:var(--white);color:#777;font-size:12px;padding:7px 10px;margin-bottom:25px}
.alerts .subscribe{display:inline-block;background:var(--red);color:var(--white);font-weight:600;font-size:14px;padding:5px 15px}
.welcome{position:absolute;left:0;top:256px;width:563px;text-align:center}
.welcome h1{font-family:"Marcellus SC",serif;font-weight:400;font-size:22px;color:#111}
.welcome p{font-family:"Source Sans 3",sans-serif;color:var(--accent);font-size:16px;margin-top:6px}
.auction{position:absolute;left:22px;width:510px;height:259px;background:var(--panel);border:1px solid var(--panel-line);border-radius:5px 5px 0 0}
.auction-head{height:37px;background:linear-gradient(#b01616,var(--red) 55%,var(--red-dark));border-radius:5px 5px 0 0;color:var(--white);font-family:Roboto,sans-serif;font-weight:700;font-size:14px;padding:11px 17px;letter-spacing:.2px}
.auction-photo{position:absolute;left:29px;top:49px;width:133px;height:87px;background:linear-gradient(180deg,#c9d5e0 0%,#dde4e8 22%,#8fa066 30%,#5d7a35 70%,#4a6127 100%);box-shadow:2px 3px 3px rgba(0,0,0,.35)}
.btn{position:absolute;left:60px;width:86px;height:28px;background:#000;border-radius:4px;color:var(--white);font-size:11.5px;display:flex;align-items:center;gap:6px;padding-left:10px;letter-spacing:.3px}
.btn b{width:16px;height:12px;background:#cfe4ef;border-radius:2px}
.auction-body{position:absolute;left:184px;top:57px;width:310px;font-size:11.5px;color:#333;line-height:16px;letter-spacing:.2px}
.auction-body .date{font-family:"Source Sans 3",sans-serif;font-weight:600;font-size:15px;letter-spacing:1px;color:#111;margin-bottom:5px}
.auction-body .bill{display:block;text-align:right;color:var(--accent);font-weight:700;font-size:13px;margin:7px 28px 8px 0}
.auction-body .label{font-weight:500;color:#111}
.pin{display:inline-block;vertical-align:-2px;margin-right:3px}
.auction-body .when{padding-left:56px}
.side-box{position:absolute;left:563px;width:256px;background:var(--panel);border:1px solid var(--panel-line);padding:14px 16px}
.side-box h2{font-family:"Source Sans 3",sans-serif;font-weight:600;font-size:22px;color:#111;margin-bottom:16px}
.featured{top:253px;height:272px;text-align:center;font-size:10.5px;color:#333;line-height:13px}
.featured h2{text-align:left}
.featured .title{font-weight:500}
.featured-photo{width:149px;height:91px;margin:14px auto 27px;border:2px solid var(--red);background:linear-gradient(180deg,#dfe8ef 0%,#b9c7a5 35%,#6f8b4c 70%,#4b6e2e 100%)}
.testimonials{top:565px;height:236px}
.quote{font-style:italic;font-size:11px;line-height:16.6px;color:#222;padding-left:6px}
.quote q{quotes:none}
.qmark{font-family:Georgia,serif;font-size:18px;color:#999;font-style:normal}
.author{color:var(--accent);font-weight:700;font-style:italic;font-size:12px;margin-top:10px;padding-left:6px}
.footer{position:absolute;top:1067px;left:0;width:831px;height:117px;background:linear-gradient(180deg,var(--red) 0%,#8a0f0f 60%,#6a0a0a 100%);color:var(--white)}
.contact{position:absolute;left:19px;top:19px;font-size:12.2px;line-height:20px}
.footer-brand{position:absolute;left:380px;top:44px;display:flex;align-items:center;gap:8px}
.footer-brand span{width:20px;height:20px;border-radius:50%;background:#c9c9c9}
.footer-brand b{font-family:"Marcellus SC",serif;font-weight:400;font-size:15px}
.badges{position:absolute;left:586px;top:34px;display:flex;gap:16px;align-items:center}
.badges i{display:block;background:#f2f2f2}
</style>
</head>
<body>
<div class="site">
  <header class="header">
    <div class="brand"><span class="brand-mark"></span><span class="brand-name">Copperfield Gavel Sales</span></div>
    <nav class="social">
      <a href="#"><span></span>Fz</a>
      <a href="#"><span></span>Chirpa</a>
      <a href="#"><span></span>Zelnix+</a>
    </nav>
  </header>

  <nav class="nav">
    <a href="#" style="width:103px">Home</a>
    <a href="#" class="active" style="width:112px">Auctions</a>
    <a href="#" style="width:173px">Auction Marketing</a>
    <a href="#" style="width:182px">Buying at Auction</a>
    <a href="#" style="width:111px">About Us</a>
    <a href="#" style="width:150px">Contact Us</a>
  </nav>
  <div class="dropdown">
    <a href="#" class="upcoming">Upcoming auctions</a>
    <a href="#" class="past">Past auctions</a>
  </div>

  <main class="main">
    <div class="slider" role="img" aria-label="Slideshow photo of a red brick two-storey house under a blue sky">
      <svg class="share" width="24" height="24" viewBox="0 0 24 24"><circle cx="12" cy="12" r="12" fill="#111"/><path d="M6 16c1-4 4-6 8-6V7l5 4.5-5 4.5v-3c-3 0-5 1-8 3z" fill="#fff"/></svg>
      <div class="dots"><i></i><i class="on"></i><i></i><i></i><i></i></div>
    </div>

    <section class="alerts">
      <h2>Auction Alerts</h2>
      <p>Please join our free mailing list to get auction alerts for upcoming events.</p>
      <span class="email">Enter Your Email</span>
      <span class="subscribe">Subscribe</span>
    </section>

    <div class="welcome">
      <h1>Welcome to Copperfield Gavel Sales</h1>
      <p>Wes Pellham, Auctioneer. LLC</p>
    </div>

    <article class="auction" style="top:329px">
      <div class="auction-head">ART, FURNITURE AND ACCESSORIES ONLINE AUCTION</div>
      <div class="auction-photo" role="img" aria-label="Photo of open grassland for sale"></div>
      <div class="btn" style="top:156px"><b></b>Details</div>
      <div class="btn" style="top:193px"><b></b>Photos</div>
      <div class="auction-body">
        <div class="date">THURSDAY, AUGUST 21ST AT 10:00 A.M.</div>
        Selling 3120 Acres of land in tracts of 2590 Acres &amp; 560 Acres
        <span class="bill">Click here to view Sale Bill!</span>
        <div class="label">LIVE OFF-SITE AUCTION</div>
        <div class="label">Auction Location:</div>
        <div><svg class="pin" width="9" height="12" viewBox="0 0 9 12"><path d="M4.5 0A4.5 4.5 0 0 0 0 4.5C0 8 4.5 12 4.5 12S9 8 9 4.5A4.5 4.5 0 0 0 4.5 0z" fill="#d01010"/><circle cx="4.5" cy="4.5" r="1.6" fill="#fff"/></svg>418 N Linden Ave, Harlowe, OK 73990</div>
        <div class="label">Property Location:</div>
        <div><svg class="pin" width="9" height="12" viewBox="0 0 9 12"><path d="M4.5 0A4.5 4.5 0 0 0 0 4.5C0 8 4.5 12 4.5 12S9 8 9 4.5A4.5 4.5 0 0 0 4.5 0z" fill="#d01010"/><circle cx="4.5" cy="4.5" r="1.6" fill="#fff"/></svg>418 N Linden Ave, Harlowe, OK 73990</div>
        <div class="when">08/21/14 at 10:00 AM CDT</div>
      </div>
    </article>

    <article class="auction" style="top:621px">
      <div class="auction-head">ART, FURNITURE AND ACCESSORIES ONLINE AUCTION</div>
      <div class="auction-photo" role="img" aria-label="Photo of open grassland for sale"></div>
      <div class="btn" style="top:156px"><b></b>Details</div>
      <div class="btn" style="top:193px"><b></b>Photos</div>
      <div class="auction-body">
        <div class="date">THURSDAY, AUGUST 21ST AT 10:00 A.M.</div>
        Selling 3120 Acres of land in tracts of 2590 Acres &amp; 560 Acres
        <span class="bill">Click here to view Sale Bill!</span>
        <div class="label">LIVE OFF-SITE AUCTION</div>
        <div class="label">Auction Location:</div>
        <div><svg class="pin" width="9" height="12" viewBox="0 0 9 12"><path d="M4.5 0A4.5 4.5 0 0 0 0 4.5C0 8 4.5 12 4.5 12S9 8 9 4.5A4.5 4.5 0 0 0 4.5 0z" fill="#d01010"/><circle cx="4.5" cy="4.5" r="1.6" fill="#fff"/></svg>418 N Linden Ave, Harlowe, OK 73990</div>
        <div class="label">Property Location:</div>
        <div><svg class="pin" width="9" height="12" viewBox="0 0 9 12"><path d="M4.5 0A4.5 4.5 0 0 0 0 4.5C0 8 4.5 12 4.5 12S9 8 9 4.5A4.5 4.5 0 0 0 4.5 0z" fill="#d01010"/><circle cx="4.5" cy="4.5" r="1.6" fill="#fff"/></svg>418 N Linden Ave, Harlowe, OK 73990</div>
        <div class="when">08/21/14 at 10:00 AM CDT</div>
      </div>
    </article>

    <aside class="side-box featured">
      <h2>Featured Auctions</h2>
      <div class="title">13.35 ACRES OF PRIME DEVELOP<br>&amp; 33RD STREET</div>
      <div class="featured-photo" role="img" aria-label="Photo of a white farmhouse with bidders gathered on the lawn"></div>
      <div>LOTS 13 &amp; 14 FOR SALE, PEMBROOK<br>IOWA<br>Third Street, Pembrook, IA 52990</div>
    </aside>

    <aside class="side-box testimonials">
      <h2>Testimonials Blog</h2>
      <p class="quote"><span class="qmark">“</span> It is a long established fact that a reader will be distracted by the readable content of a page when looking at its layout. The point of using Lorem Ipsum is that it has a more-or-less normal distribution of letters, as opposed to using. <span class="qmark">”</span></p>
      <p class="author">Marla Denson</p>
    </aside>
  </main>

  <footer class="footer">
    <div class="contact">
      Copperfield Gavel Sales, LLC / Wes Pellham<br>
      email: wespell@mailbox.example; wes.pellham@ml7.example<br>
      phone: (859) 555-0147 mobile phone: (859)555-0182<br>
      Copyright © 2014: Copperfield Gavel Sales. LLC
    </div>
    <div class="footer-brand"><span></span><b>Copperfield Gavel Sales</b></div>
    <div class="badges">
      <i style="width:38px;height:42px"></i>
      <i style="width:72px;height:38px;border-radius:4px"></i>
      <i style="width:80px;height:34px;border-radius:50%"></i>
    </div>
  </footer>
</div>
</body>
</html>
```